Website Design

Hi I would like to invite designers to re design my website .

I would like the below in brief.

On the Welcome Page.

A nice looking technical page distributed into two

SALES on one side and TECHNOLOGY on the other . once the person clicks on either of them they can explore the pages in detail.

I am keen and almost ready with information for the Technology page and would like this to begin kicking ASAP .

my current website is www.brimvoltek.net

Looking forward to seeing your feedback!

Tobiah
Updates

Hi,

 
A little more elaboration on the web front page . I need it to be more techy .

I was looking at a wheel on the Technical side or a spanner and screew driver done on flash .

Just to give you a better idea on what seperated Sales from Technology. 

Computing, Storage , Components , Peripherals , Software , TV & Gaming / Entertainment , Home & Leisure , Software , Gift Vouchers , Phones etc.

Technology .

Solar Power Solutions , Security Systems , Access Control , Automatic Gates & Turnstiles , Home/Office/Hotel Automation, Indoor and Outdoor PABX Telephony, Networking , Electricity Power Meters , IP Based Technology and ETC. 

See attached on the project updates my business card design if it can give you an idea ,also see revised Logo

```html
<!DOCTYPE html>
<html lang="en">
<head>
<meta charset="utf-8">
<title>Brimvoltek – Welcome</title>
<link rel="stylesheet" href="https://fonts.googleapis.com/css2?family=Figtree:wght@400;600&family=Ubuntu:ital,wght@0,400;0,500;0,700;1,400&display=swap">
<style>
  :root{
    --topbar-bg:#f5f5f5;
    --header-bg:#f7f7f7;
    --rule:#dcdcdc;
    --muted:#8a8a8a;
    --nav:#9a9a9a;
    --accent:#c0393b;
    --ink:#1c1c1c;
    --navy:#1c2630;
    --red-deep:#a8191c;
    --red-mid:#cc3d3a;
    --red-light:#e0605a;
    --white:#ffffff;
    --social:#d4d4d4;
  }
  *{box-sizing:border-box;margin:0;padding:0}
  html,body{width:1200px;height:599px;overflow:hidden;background:var(--white)}
  body{position:relative;font-family:"Figtree",sans-serif}

  .topbar{position:absolute;left:0;top:0;width:1200px;height:32px;background:var(--topbar-bg);border-bottom:1px solid var(--rule)}
  .topbar__contact{position:absolute;left:125px;top:8px;font-family:"Ubuntu",sans-serif;font-style:italic;font-size:10.5px;color:var(--muted)}
  .topbar__social{position:absolute;left:948px;top:5px;display:flex;gap:10.5px}
  .topbar__social span{width:22px;height:22px;border-radius:3px;background:var(--social)}

  .header{position:absolute;left:0;top:32px;width:1200px;height:100px;background:var(--header-bg)}
  .brand{position:absolute;left:125px;top:30px;display:flex;align-items:center;gap:10px;font-family:"Figtree",sans-serif;font-weight:600;font-size:36px;color:var(--accent);letter-spacing:.5px}
  .brand__mark{width:14px;height:14px;border-radius:50%;background:var(--accent)}
  .nav{position:absolute;top:0;left:0;height:100px;width:1200px}
  .nav a{position:absolute;top:30px;font-family:"Ubuntu",sans-serif;font-weight:500;font-size:10.5px;letter-spacing:1.6px;color:var(--nav);text-decoration:none}
  .nav a.is-active{color:var(--accent)}
  .nav__indicator{position:absolute;left:426px;top:0;width:62px;height:3px;background:var(--accent)}
  .header__divider{position:absolute;top:0;width:1px;height:75px;background:var(--rule)}
  .search{position:absolute;left:1029px;top:30px}

  .hero{position:absolute;left:0;top:132px;width:1200px;height:420px}
  .hero__sales{position:absolute;left:0;top:0;width:600px;height:420px;background:var(--navy)}
  .hero__tech{position:absolute;left:600px;top:0;width:600px;height:420px;
    background:radial-gradient(ellipse at 20% 15%,var(--red-light) 0%,transparent 55%),
               linear-gradient(160deg,var(--red-mid) 0%,var(--red-deep) 55%,var(--red-mid) 100%)}

  .sales__title{position:absolute;left:86px;top:100px;font-weight:600;font-size:90px;line-height:1;color:var(--white);letter-spacing:-.5px}
  .sales__rule{position:absolute;left:87px;top:200px}
  .sales__tagline{position:absolute;left:87px;top:222px;font-weight:400;font-size:26px;color:var(--white)}

  .tech__title{position:absolute;left:0;width:600px;top:95px;text-align:center;font-family:"Ubuntu",sans-serif;font-weight:500;font-size:34px;color:var(--white)}
  .tech__timeline{position:absolute;left:0;top:158px}
  .tech__step{position:absolute;width:120px;margin-left:-60px;top:183px;text-align:center;color:var(--white)}
  .tech__step svg{display:block;margin:0 auto 10px}
  .tech__step span{font-family:"Ubuntu",sans-serif;font-weight:700;font-size:14px}

  .hero__cta{position:absolute;left:512px;top:355px;width:176px;height:40px;border:1.5px solid var(--white);border-radius:3px;display:flex;align-items:center;justify-content:center;font-family:"Figtree",sans-serif;font-weight:600;font-size:12.5px;color:var(--white);text-decoration:none;letter-spacing:.3px}
</style>
</head>
<body>
  <div class="topbar">
    <p class="topbar__contact">Email Us: hello@brimvoltek.net | Call Us: 555-014-2286</p>
    <div class="topbar__social" aria-label="Social links"><span></span><span></span><span></span><span></span></div>
  </div>

  <header class="header">
    <div class="brand"><span class="brand__mark"></span>Brimvoltek</div>
    <nav class="nav">
      <span class="nav__indicator"></span>
      <a href="#" class="is-active" style="left:438px">HOME</a>
      <a href="#" style="left:507px">PORTFOLIO</a>
      <a href="#" style="left:610px">BLOG</a>
      <a href="#" style="left:675px">PAGES</a>
      <a href="#" style="left:747px">SHOP</a>
      <a href="#" style="left:813px">MEGA MENU</a>
      <a href="#" style="left:921px">CONTACT</a>
    </nav>
    <span class="header__divider" style="left:999px"></span>
    <span class="header__divider" style="left:1072px"></span>
    <svg class="search" width="16" height="16" viewBox="0 0 16 16" aria-label="Search">
      <circle cx="6.5" cy="6.5" r="4.8" fill="none" stroke="#8a8a8a" stroke-width="1.6"/>
      <line x1="10" y1="10" x2="14" y2="14" stroke="#8a8a8a" stroke-width="1.8" stroke-linecap="round"/>
    </svg>
  </header>

  <section class="hero">
    <div class="hero__sales">
      <h1 class="sales__title">SALES</h1>
      <svg class="sales__rule" width="310" height="12" viewBox="0 0 310 12">
        <polyline points="0,1 147,1 155,9 163,1 310,1" fill="none" stroke="#5a6570" stroke-width="1"/>
      </svg>
      <p class="sales__tagline">Visit our Shop Now</p>
    </div>

    <div class="hero__tech" role="img" aria-label="Close-up photograph of a red circuit board">
      <h2 class="tech__title">TECHNOLOGY</h2>
      <svg class="tech__timeline" width="600" height="16" viewBox="0 0 600 16">
        <line x1="162" y1="8" x2="432" y2="8" stroke="#ffffff" stroke-width="1"/>
        <circle cx="157" cy="8" r="5" fill="#c23531" stroke="#fff" stroke-width="1.6"/>
        <circle cx="297" cy="8" r="5" fill="#c23531" stroke="#fff" stroke-width="1.6"/>
        <circle cx="437" cy="8" r="5" fill="#c23531" stroke="#fff" stroke-width="1.6"/>
      </svg>
      <div class="tech__step" style="left:161px">
        <svg width="26" height="26" viewBox="0 0 26 26"><rect x="3" y="2" width="2.6" height="23" fill="#fff"/><path d="M6 3h9l1.5 3H24l-3 5 3 5h-9l-1.5-3H6z" fill="#fff"/></svg>
        <span>Branding</span>
      </div>
      <div class="tech__step" style="left:304px">
        <svg width="26" height="26" viewBox="0 0 26 26"><rect x="2" y="2" width="22" height="22" rx="4" fill="none" stroke="#fff" stroke-width="2.4"/><rect x="8" y="8" width="3.5" height="3.5" fill="#fff"/><rect x="14.5" y="8" width="3.5" height="3.5" fill="#fff"/><rect x="8" y="14.5" width="3.5" height="3.5" fill="#fff"/><rect x="14.5" y="14.5" width="3.5" height="3.5" fill="#fff"/></svg>
        <span>UX Design</span>
      </div>
      <div class="tech__step" style="left:442px">
        <svg width="26" height="26" viewBox="0 0 26 26"><g fill="#fff"><circle cx="13" cy="13" r="8"/><rect x="11" y="1" width="4" height="24" rx="1"/><rect x="1" y="11" width="24" height="4" rx="1"/><rect x="11" y="1" width="4" height="24" rx="1" transform="rotate(45 13 13)"/><rect x="11" y="1" width="4" height="24" rx="1" transform="rotate(-45 13 13)"/></g><circle cx="13" cy="13" r="3.5" fill="#c23531"/></svg>
        <span>Develop</span>
      </div>
    </div>

    <a href="#" class="hero__cta">VIEW WORK</a>
  </section>
</body>
</html>
```